A modern web page for a software product

We need a web page for a software product, which is an advanced solution based on Machine Learning and Natural Language processing. We already have a logo of the product and expect the web page to be inline with the logo colors. The design should be for one page web site with scrolled sections - details of the content and guidelines in the attachments.

Target Market(s)

software company

Industry/Entity Type

It Company

Number of Pages Required

1 page

Colors

Designer to choose colors to be used in the design.

Requirements
Must have
• - modern icons and graphics
• - inline with the logo colors
• - be related to Machine Learining, AI, data processing
• - should have two language versions: english and polish both are attached.
Nice to have
• - animation/motion
Should not have
• - any photos embedded

```html
<!DOCTYPE html>
<html lang="en">
<head>
<meta charset="utf-8">
<title>Personal Data Detection – Product</title>
<link href="https://fonts.googleapis.com/css2?family=Lato:wght@300;400&display=swap" rel="stylesheet">
<style>
  :root {
    --navy: #173a6e;
    --teal: #13b9b5;
    --cyan: #1fd0da;
    --ink: #3b3f45;
    --muted: #8e969e;
    --rule: #e6e8ea;
    --band-top: #5c739a;
    --band-bottom: #2c4a7b;
    --card: #eeeff0;
    --icon-grey: #c7ccd4;
    --white: #ffffff;
  }
  * { box-sizing: border-box; margin: 0; padding: 0; }
  html, body { width: 944px; height: 1200px; overflow: hidden; background: var(--white); }
  body { position: relative; font-family: "Lato", sans-serif; font-weight: 300; color: var(--ink); }

  .feature { position: absolute; left: 0; top: 0; width: 944px; text-align: center; }
  .feature__icon { position: absolute; left: 429px; top: 30px; width: 86px; height: 86px; border-radius: 50%; background: var(--navy); display: flex; align-items: center; justify-content: center; }
  .feature__title { position: absolute; top: 128px; width: 100%; font-size: 15px; font-weight: 400; color: var(--ink); }
  .feature__text { position: absolute; top: 157px; left: 342px; width: 260px; font-size: 13px; line-height: 22px; color: var(--muted); }
  .divider { position: absolute; left: 0; top: 252px; width: 944px; height: 1px; background: var(--rule); }

  .section-title { position: absolute; width: 944px; text-align: center; font-size: 23px; font-weight: 300; letter-spacing: 0.3px; color: var(--ink); }
  .section-title--use { top: 296px; }
  .section-title--high { top: 743px; }

  .use-cases { position: absolute; left: 0; top: 359px; width: 944px; height: 332px; background: linear-gradient(var(--band-top), var(--band-bottom)); box-shadow: inset 0 3px 3px rgba(0,0,0,0.12); }
  .use-case { position: absolute; top: 60px; width: 180px; text-align: center; }
  .use-case__ring { width: 137px; height: 137px; margin: 0 auto; border: 2px solid var(--white); border-radius: 50%; display: flex; align-items: center; justify-content: center; }
  .use-case__text { margin-top: 16px; font-size: 13px; font-weight: 400; line-height: 16.3px; color: var(--white); }
  .use-case--audit { left: 106px; }
  .use-case--catalog { left: 381px; }
  .use-case--registry { left: 656px; }
  .carousel-arrow { position: absolute; top: 133px; width: 48px; height: 48px; border: 2px solid var(--white); border-radius: 50%; display: flex; align-items: center; justify-content: center; }
  .carousel-arrow--prev { left: 37px; }
  .carousel-arrow--next { left: 859px; }

  .highlight { position: absolute; top: 878px; width: 395px; height: 256px; background: var(--card); }
  .highlight--polish { left: 69px; }
  .highlight--methods { left: 480px; }
  .highlight__badge { position: absolute; top: -34px; left: 164px; width: 67px; height: 67px; border-radius: 50%; background: var(--teal); border: 2px solid #d9dcdf; overflow: hidden; }
  .highlight__title { position: absolute; top: 47px; left: 15px; right: 15px; text-align: center; font-size: 15.5px; line-height: 19px; font-weight: 300; color: var(--ink); text-transform: uppercase; }
  .highlight__list { position: absolute; top: 113px; left: 17px; right: 20px; list-style: none; font-size: 13px; line-height: 21.8px; color: var(--muted); }
</style>
</head>
<body>

<section class="feature">
  <div class="feature__icon">
    <svg width="22" height="22" viewBox="0 0 24 24" aria-hidden="true">
      <g fill="var(--cyan)">
        <circle cx="12" cy="12" r="7"/>
        <rect x="10.2" y="1.5" width="3.6" height="21" rx="1"/>
        <rect x="10.2" y="1.5" width="3.6" height="21" rx="1" transform="rotate(45 12 12)"/>
        <rect x="10.2" y="1.5" width="3.6" height="21" rx="1" transform="rotate(90 12 12)"/>
        <rect x="10.2" y="1.5" width="3.6" height="21" rx="1" transform="rotate(135 12 12)"/>
      </g>
      <circle cx="12" cy="12" r="4.2" fill="var(--navy)"/>
      <circle cx="12" cy="12" r="2.2" fill="var(--cyan)"/>
    </svg>
  </div>
  <h3 class="feature__title">RESTful API</h3>
  <p class="feature__text">RESTful API for system management and integration</p>
</section>

<div class="divider"></div>

<h2 class="section-title section-title--use">USE CASES</h2>

<section class="use-cases">
  <div class="carousel-arrow carousel-arrow--prev">
    <svg width="14" height="18" viewBox="0 0 14 18" aria-hidden="true"><path d="M10 2 L4 9 L10 16" fill="none" stroke="var(--white)" stroke-width="3" stroke-linecap="round" stroke-linejoin="round"/></svg>
  </div>

  <div class="use-case use-case--audit">
    <div class="use-case__ring">
      <svg width="70" height="84" viewBox="0 0 70 84" aria-hidden="true">
        <path d="M8 10 H40 M8 10 V80 H62 V34" fill="none" stroke="var(--icon-grey)" stroke-width="5"/>
        <path d="M14 16 H36 M14 16 V74 H56 V38" fill="none" stroke="var(--icon-grey)" stroke-width="1.5"/>
        <path d="M44 30 L64 6 L68 10 L48 34 L42 36 Z" fill="var(--icon-grey)"/>
        <circle cx="31" cy="48" r="9" fill="none" stroke="var(--icon-grey)" stroke-width="4.5"/>
        <path d="M38 55 L47 64" stroke="var(--icon-grey)" stroke-width="6" stroke-linecap="round"/>
      </svg>
    </div>
    <p class="use-case__text">Internal audits and verification of the current status - in preparation for ensuring RODO compliance RODO</p>
  </div>

  <div class="use-case use-case--catalog">
    <div class="use-case__ring">
      <svg width="94" height="74" viewBox="0 0 94 74" aria-hidden="true">
        <path d="M40 8 C34 2 44 0 46 6 C48 12 56 10 54 18" fill="none" stroke="var(--icon-grey)" stroke-width="1.5" stroke-dasharray="3 2"/>
        <rect x="54" y="18" width="24" height="46" rx="12" transform="rotate(-45 66 41)" fill="var(--icon-grey)"/>
        <rect x="14" y="26" width="24" height="46" rx="6" transform="rotate(40 26 49)" fill="#a9b0bb"/>
        <rect x="18" y="22" width="24" height="46" rx="6" transform="rotate(40 30 45)" fill="var(--icon-grey)"/>
        <circle cx="40" cy="28" r="3" fill="#4d6590"/>
      </svg>
    </div>
    <p class="use-case__text">Cataloging sources that store sensitive data</p>
  </div>

  <div class="use-case use-case--registry">
    <div class="use-case__ring">
      <svg width="54" height="46" viewBox="0 0 54 46" aria-hidden="true">
        <path d="M27 24 L18 14 H24 V6 C24 2 28 0 32 2 C28 3 30 6 30 8 V14 H36 Z" fill="var(--icon-grey)"/>
        <path d="M2 30 L10 18 H16 L19 22 H12 L8 29 H18 L21 34 H33 L36 29 H46 L42 22 H35 L38 18 H44 L52 30 V44 H2 Z" fill="var(--icon-grey)"/>
      </svg>
    </div>
    <p class="use-case__text">Keeping the registry of personal data in order to implement rights to information, forgetfulness, data transfer</p>
  </div>

  <div class="carousel-arrow carousel-arrow--next">
    <svg width="14" height="18" viewBox="0 0 14 18" aria-hidden="true"><path d="M4 2 L10 9 L4 16" fill="none" stroke="var(--white)" stroke-width="3" stroke-linecap="round" stroke-linejoin="round"/></svg>
  </div>
</section>

<h2 class="section-title section-title--high">HIGHLIGHTS</h2>

<article class="highlight highlight--polish">
  <div class="highlight__badge">
    <svg width="63" height="63" viewBox="0 0 63 63" aria-hidden="true">
      <path d="M31.5 10 C24 10 22 17 23 24 C23.5 30 27 36 31.5 36 C36 36 39.5 30 40 24 C41 17 39 10 31.5 10 Z" fill="var(--navy)"/>
      <path d="M26 35 C20 39 12 40 11 48 V63 H52 V48 C51 40 43 39 37 35 C35 38 28 38 26 35 Z" fill="var(--navy)"/>
    </svg>
  </div>
  <h3 class="highlight__title">Built in support for detection of Polish personal data</h3>
  <ul class="highlight__list">
    <li>a. sensitive data type (eg.:ID, name, address, etc.)</li>
    <li>b. context of data occurrence</li>
    <li>c. metadata describing the data source (e.g. system, table, author, etc.) d. metadata describing the detection process</li>
  </ul>
</article>

<article class="highlight highlight--methods">
  <div class="highlight__badge">
    <svg width="63" height="63" viewBox="0 0 63 63" aria-hidden="true">
      <path d="M41 14 C36 14 34 19 35 24 C35.5 29 38 32 41 32 C44 32 46.5 29 47 24 C48 19 46 14 41 14 Z" fill="var(--navy)"/>
      <path d="M36 31 C33 34 30 36 30 44 V63 H58 V44 C57 37 51 35 46 31 C44 34 38 34 36 31 Z" fill="var(--navy)"/>
      <path d="M25 11 C19 11 17 16 18 22 C18.5 27 21 31 25 31 C29 31 31.5 27 32 22 C33 16 31 11 25 11 Z" fill="var(--navy)" stroke="var(--teal)" stroke-width="1.5"/>
      <path d="M20 30 C15 33 7 35 7 43 V63 H43 V43 C42 35 35 33 30 30 C28 33 22 33 20 30 Z" fill="var(--navy)" stroke="var(--teal)" stroke-width="1.5"/>
    </svg>
  </div>
  <h3 class="highlight__title">High effectiveness of personal data detection (also "noisy" data) by</h3>
  <ul class="highlight__list">
    <li>a. Natural Language Processing</li>
    <li>b. Machine Learning</li>
    <li>c. expert rules</li>
    <li>d. custom models for data detection specific to your organization needs</li>
  </ul>
</article>

</body>
</html>
```